Bradwell Business Card

I have a logo that I would like to use to design the Business Card for Bradwell Construction LLC. We are a commercial general contractor in San Antonio Texas. Id like a simple and sleek design. Message me if you have any questions. Thanks

Industry/Entity Type

Contractor

```html
<!DOCTYPE html>
<html lang="en">
<head>
<meta charset="utf-8">
<title>Bradwell Construction LLC — Business Card</title>
<link rel="stylesheet" href="https://fonts.googleapis.com/css2?family=Archivo+Black&family=Roboto:wght@400;500&display=swap">
<style>
  :root {
    --backdrop: #2b2b2d;
    --card: #ffffff;
    --ink: #1a1a1a;
    --muted: #555555;
    --brand-blue: #2f6bc4;
    --divider: #b9b9b9;
  }
  * { box-sizing: border-box; margin: 0; padding: 0; }
  html, body { width: 1200px; height: 900px; overflow: hidden; }
  body {
    background: var(--backdrop);
    font-family: "Roboto", Arial, sans-serif;
    display: flex;
    align-items: center;
    justify-content: center;
    gap: 60px;
  }
  .card {
    position: relative;
    width: 525px;
    height: 300px;
    background: var(--card);
    box-shadow: 0 10px 30px rgba(0,0,0,0.45);
    overflow: hidden;
  }

  /* Front */
  .card--front {
    display: flex;
    flex-direction: column;
    align-items: center;
    justify-content: center;
  }
  .brand {
    display: flex;
    align-items: center;
    gap: 12px;
  }
  .brand__dot {
    width: 16px;
    height: 16px;
    border-radius: 50%;
    background: var(--brand-blue);
    flex: none;
  }
  .brand__name {
    font-family: "Archivo Black", "Arial Black", sans-serif;
    color: var(--ink);
    text-transform: uppercase;
    line-height: 0.95;
    letter-spacing: -0.5px;
  }
  .card--front .brand__name { font-size: 27px; }
  .front__web {
    margin-top: 46px;
    font-size: 12px;
    color: var(--ink);
  }
  .front__web .accent { color: var(--brand-blue); }

  /* Back */
  .card--back { display: flex; }
  .back__logo {
    width: 50%;
    display: flex;
    align-items: center;
    justify-content: center;
    padding-bottom: 40px;
  }
  .card--back .brand__name { font-size: 21px; }
  .back__divider {
    position: absolute;
    left: 262px;
    top: 70px;
    width: 1px;
    height: 120px;
    background: linear-gradient(to bottom, transparent, var(--divider), transparent);
  }
  .contact {
    width: 50%;
    padding: 78px 0 0 22px;
  }
  .contact__name {
    font-size: 19px;
    color: var(--brand-blue);
  }
  .contact__role {
    font-size: 11px;
    color: var(--muted);
    margin: 3px 0 14px;
  }
  .contact__address {
    font-size: 11px;
    color: var(--muted);
    line-height: 1.4;
    margin-bottom: 8px;
  }
  .contact__line {
    display: flex;
    align-items: center;
    gap: 7px;
    font-size: 11px;
    color: var(--muted);
    line-height: 1.45;
  }
  .contact__line svg { width: 9px; height: 9px; fill: var(--brand-blue); flex: none; }
  .back__band {
    position: absolute;
    left: 0; right: 0; bottom: 0;
    height: 16px;
    background: var(--brand-blue);
  }
  .back__notch {
    position: absolute;
    left: 254px;
    bottom: 15px;
    width: 18px;
    height: 10px;
  }
</style>
</head>
<body>

  <section class="card card--front" aria-label="Card front">
    <div class="brand">
      <span class="brand__dot"></span>
      <div class="brand__name">Bradwell<br>Construction LLC</div>
    </div>
    <p class="front__web">www.<span class="accent">bradwellbuild</span>.com</p>
  </section>

  <section class="card card--back" aria-label="Card back">
    <div class="back__logo">
      <div class="brand">
        <span class="brand__dot"></span>
        <div class="brand__name">Bradwell<br>Construction LLC</div>
      </div>
    </div>
    <div class="back__divider"></div>
    <div class="contact">
      <h1 class="contact__name">Daniel Reyes</h1>
      <p class="contact__role">Occupation</p>
      <p class="contact__address">Suite 200, 410 Alamo Plaza<br>Riverwalk Business Park</p>
      <p class="contact__line">
        <svg viewBox="0 0 10 10"><path d="M2 0.5 L3.8 2.6 L2.9 3.6 Q4 5.8 6.4 7.1 L7.4 6.2 L9.5 8 L8.2 9.5 Q3.5 9 0.5 1.8 Z"/></svg>
        000 000 0000
      </p>
      <p class="contact__line">
        <svg viewBox="0 0 10 10"><path d="M0.5 2 H9.5 V8 H0.5 Z M1 2.4 L5 5.6 L9 2.4" fill="none" stroke="#2f6bc4" stroke-width="1"/></svg>
        dreyes@bradwellbuild.com
      </p>
      <p class="contact__line">
        <svg viewBox="0 0 10 10"><circle cx="5" cy="5" r="4.5"/></svg>
        www.bradwellbuild.com
      </p>
    </div>
    <svg class="back__notch" viewBox="0 0 18 10" aria-hidden="true"><path d="M0 10 L9 0 L18 10 Z" fill="#2f6bc4"/></svg>
    <div class="back__band"></div>
  </section>

</body>
</html>
```